Background on the company
=======================
This is a Bitcoin Consulting Company.

We have two projects.

Tinted Tokens: software to trade assets over the Bitcoin protocol (assets like property, traditional currencies, gold, stocks, securities, bonds, etc.).

Quarnix Private Vaulter: a hardware based web service in a box that manages cold storage wallets and off line transaction signing. It is the secure way to deploy a web wallet without relying on third parties.

All that to say this is a high tech company focusing on Bitcoin.

What does Fellowdrim mean?
========================

The Beast of Fellowdrim is the rabbit in Jasper Quill's Silver Chalice that defeats his band of knights. (At least until they go and get the Sacred Pocket Rocket).

We like this, because we are a deceptively soft and fuzzy company that is also killer!

What We Need:
============

Primarily we need to get the logo designed. I have a hand drawing I did, but you are not limited to that. And the logo needs to work on a business card. The right logo that works on a Business Card is the primary consideration.
Updates

The main task here is to get the logo right.  I have provided a drawing I made, and I like it, but my complaints are:  Fellowdrim is hard to read.  The 'C' isn't obvious.

We can fix this many ways.  We can forget the whole "combinde a rabit with the C and a" idea.  We can add "Fellowdrim Systems" on the card apart from the logo (that way if they don't "get it" they can still read it.)

The Rabbit itself is quite obviously scanned from a hand drawing.  That might not be a bad thing, but combine that with the entire logo, and it is too cheap looking.

Target Market(s)

Technical folks. Investors. Business contacts.

Industry/Entity Type

Software

Requirements
Must have
• We have to clean up the logo, or replace it with something that hints at the same sort of things. (See the upload) Basically and innocent white bunny. Something that works on a Business Card.

All the information below:

Derek Haldane
ph (555) 304-1927
haldane.derek@mailvista.example
derek@fellowdrim.example
Nice to have
• I would like it to be serious, yet whimsical. An inside joke, so you get it if you know Jasper Quill. But otherwise, it looks reasonably serious if you don't know Jasper Quill.

I don't want it to be scary. (oddly, that my own efforts seem to make that easy to do)

Would like a set of colors that remind one of a cave, a rabbit, knights.... Not sure what those are...

```html
<!DOCTYPE html>
<html lang="en">
<head>
<meta charset="utf-8">
<title>Fellowdrim – Business Card</title>
<link rel="stylesheet" href="https://fonts.googleapis.com/css2?family=PT+Sans:ital,wght@0,400;0,700;1,700&display=swap">
<style>
  :root {
    --backdrop: #e9e6e2;
    --card-top: #ffffff;
    --card-bottom: #e4e4e4;
    --brand-red: #c8102e;
    --deep-red: #b01227;
    --orange-light: #fbb03b;
    --orange: #f7941d;
    --orange-deep: #ee7a12;
    --ink: #2b2b2b;
    --ink-soft: #555555;
  }
  html, body {
    margin: 0;
    width: 1200px;
    height: 900px;
    overflow: hidden;
    background: var(--backdrop);
  }
  .canvas {
    width: 1200px;
    height: 900px;
    display: flex;
    align-items: center;
    justify-content: center;
  }
  .business-card {
    width: 1000px;
    height: 571px;
    display: block;
    filter: drop-shadow(0 10px 22px rgba(0,0,0,0.25));
    font-family: "PT Sans", Arial, sans-serif;
  }
  .card-face { fill: url(#cardSheen); }
  .top-edge { fill: var(--brand-red); }
  .swoosh-red { fill: var(--brand-red); }
  .swoosh-deep { fill: var(--deep-red); }
  .swoosh-orange { fill: url(#orangeFlow); }
  .brand-name { fill: var(--brand-red); font-size: 54px; font-weight: 400; }
  .brand-dot { fill: var(--brand-red); }
  .contact-line { fill: var(--ink); font-size: 23px; }
  .contact-icon { fill: var(--ink); }
  .contact-icon-line { stroke: var(--ink); stroke-width: 2; fill: none; }
  .person-name { fill: var(--brand-red); font-size: 40px; font-weight: 700; }
  .person-title { fill: var(--ink-soft); font-size: 27px; }
  .slogan { fill: var(--deep-red); font-size: 21px; font-weight: 700; font-style: italic; }
</style>
</head>
<body>
<main class="canvas">
  <svg class="business-card" viewBox="0 0 1000 571" xmlns="http://www.w3.org/2000/svg" aria-label="Fellowdrim business card for Derek Haldane">
    <defs>
      <linearGradient id="cardSheen" x1="0" y1="0" x2="0.3" y2="1">
        <stop offset="0" stop-color="var(--card-top)"/>
        <stop offset="1" stop-color="var(--card-bottom)"/>
      </linearGradient>
      <linearGradient id="orangeFlow" x1="0" y1="0" x2="1" y2="1">
        <stop offset="0" stop-color="var(--orange-light)"/>
        <stop offset="0.5" stop-color="var(--orange)"/>
        <stop offset="1" stop-color="var(--orange-deep)"/>
      </linearGradient>
      <clipPath id="cardShape"><rect width="1000" height="571" rx="6"/></clipPath>
    </defs>

    <g clip-path="url(#cardShape)">
      <rect class="card-face" width="1000" height="571"/>
      <rect class="top-edge" width="1000" height="5"/>

      <path class="swoosh-red" d="M0 314 C250 324 450 388 700 392 C820 394 920 376 1000 364 L1000 378 C900 398 800 410 700 409 C450 406 250 342 0 338 Z"/>
      <path class="swoosh-orange" d="M0 358 C250 370 460 434 720 428 C850 424 940 408 1000 396 L1000 571 L0 571 Z"/>
      <path class="swoosh-deep" d="M0 392 C300 412 520 468 1000 444 L1000 458 C520 484 300 428 0 406 Z"/>
    </g>

    <g class="brand">
      <circle class="brand-dot" cx="68" cy="82" r="9"/>
      <text class="brand-name" x="88" y="100">Fellowdrim</text>
    </g>

    <g class="contacts">
      <g class="contact-icon-set">
        <path class="contact-icon" d="M104 132 c3 -2 6 -1 7 2 l3 5 c1 2 0 4 -2 5 l-2 1 c1 4 4 7 8 9 l1 -2 c1 -2 3 -3 5 -2 l5 3 c3 1 3 4 1 7 c-3 3 -8 4 -13 1 c-7 -4 -13 -11 -15 -18 c-1 -5 0 -9 2 -11 Z"/>
        <rect class="contact-icon" x="102" y="172" width="26" height="16" rx="2"/>
        <rect class="contact-icon-line" x="107" y="164" width="16" height="9"/>
        <rect class="contact-icon" x="107" y="195" width="16" height="26" rx="3"/>
        <rect class="contact-icon" x="102" y="229" width="26" height="18" rx="2"/>
        <path d="M103 231 L115 240 L127 231" stroke="#fff" stroke-width="2" fill="none"/>
        <circle class="contact-icon" cx="115" cy="266" r="12"/>
        <path d="M103 266 H127 M115 254 C108 261 108 271 115 278 M115 254 C122 261 122 271 115 278" stroke="#fff" stroke-width="1.5" fill="none"/>
      </g>
      <text class="contact-line" x="142" y="155">(555) 304-1927</text>
      <text class="contact-line" x="142" y="185">(555) 304-1927</text>
      <text class="contact-line" x="142" y="215">(555) 304-1927</text>
      <text class="contact-line" x="142" y="245">haldane.derek@mailvista.example, derek@fellowdrim.example</text>
      <text class="contact-line" x="142" y="275">www.fellowdrim.example</text>
    </g>

    <g class="person" text-anchor="end">
      <text class="person-name" x="915" y="218">Derek Haldane</text>
      <text class="person-title" x="915" y="252">Director</text>
    </g>

    <text class="slogan" x="930" y="525" text-anchor="end">Your Slogan goes here!</text>
  </svg>
</main>
</body>
</html>
```